Fitness Equipment Repair Business Needs a Catchy New Business Card

We have an existing business card, however, it is quite plain and boring. We are expanding primarily in the commercial area (gyms, studios, apartment complexes etc). The business card will serve as eye candy to those managers/owners that can't be met for a face to face.
Originally I was planning for a brochure as well, but all of our information is better summarized on our website. (brasswheelservicing.ca).
I would like the card to match the colour scheme of the website and utilize the logo. It should have a professional clean feel to it, however, a little colouring outside the lines wouldn't hurt.
The example card is for my service technician (Corwin Haldane). If possible I would like to be able to edit the text to use for more than one person.

Industry/Entity Type

Appliance Repair

Contact Information for Business Card

Clean, crisp and professional but needs to be eye catching. Preferably using the black, white and red colour scheme matching the website. Double sided would be nice, but is not necessary.

Colors
ec1f27
ffffff
000000

Requirements
Must have
• Must be able to edit name, phone number and title to use for multiple people. Must show the company website (brasswheelservicing.ca).

```html
<!DOCTYPE html>
<html lang="en">
<head>
<meta charset="utf-8">
<title>Brass Wheel Servicing – Business Card</title>
<link rel="stylesheet" href="https://fonts.googleapis.com/css2?family=Cinzel:wght@400&family=Source+Sans+3:wght@400;600;700&display=swap">
<style>
  :root {
    --brand-red: #ec1f27;
    --white: #ffffff;
    --black: #000000;
    --ink: #1c1c1c;
    --stage: #e9e7e4;
    --dark-center: #5a5a5a;
    --dark-edge: #1b1b1b;
  }
  * { box-sizing: border-box; margin: 0; padding: 0; }
  html, body { width: 1200px; height: 900px; overflow: hidden; }
  body {
    position: relative;
    background: var(--stage);
    font-family: "Source Sans 3", Arial, sans-serif;
  }
  .card {
    position: absolute;
    overflow: hidden;
    box-shadow: 0 6px 18px rgba(0,0,0,0.18);
  }

  /* Front side */
  .card-front {
    left: 237px; top: 61px; width: 556px; height: 343px;
    background: var(--white);
  }
  .company-title {
    position: absolute; left: 28px; top: 32px;
    font-family: "Cinzel", "Times New Roman", serif;
    font-size: 36px; font-weight: 400; letter-spacing: 0.8px;
    color: var(--black); white-space: nowrap;
  }
  .person-name {
    position: absolute; left: 30px; top: 100px;
    font-size: 19px; font-weight: 600; color: var(--brand-red);
  }
  .person-role {
    position: absolute; left: 30px; top: 123px;
    font-size: 15px; color: var(--ink);
  }
  .contact-band {
    position: absolute; left: 0; top: 159px; width: 100%; height: 168px;
    background: var(--brand-red); color: var(--white);
  }
  .address {
    position: absolute; left: 30px; top: 16px;
    font-size: 15px; line-height: 20px;
  }
  .contact-list {
    position: absolute; left: 30px; top: 71px;
    list-style: none; font-size: 15px; line-height: 20px;
  }
  .contact-list li { display: flex; align-items: center; gap: 8px; }
  .contact-list svg { width: 11px; height: 11px; fill: var(--white); flex: none; }
  .brand-mark-front {
    position: absolute; left: 410px; top: 134px;
    font-size: 32px; font-weight: 700; letter-spacing: 1px; line-height: 1;
    color: var(--white);
  }

  /* Back side */
  .card-back {
    left: 457px; top: 517px; width: 560px; height: 344px;
    background: radial-gradient(ellipse at 45% 40%, var(--dark-center) 0%, #333 45%, var(--dark-edge) 100%);
    color: var(--white);
  }
  .brand-mark-back {
    position: absolute; left: 124px; top: 212px;
    font-size: 32px; font-weight: 700; letter-spacing: 1px; line-height: 1;
    color: var(--white);
  }
  .company-stack {
    position: absolute; left: 260px; top: 86px;
    font-family: "Cinzel", "Times New Roman", serif;
    font-size: 40px; font-weight: 400; line-height: 56px;
    letter-spacing: 0.5px;
  }
  .tagline {
    position: absolute; left: 0; top: 275px; width: 100%;
    text-align: center; font-size: 15px;
  }
</style>
</head>
<body>

<section class="card card-front" aria-label="Business card front">
  <h1 class="company-title">Brass Wheel Servicing</h1>
  <p class="person-name">Corwin Haldane</p>
  <p class="person-role">Managing Director</p>

  <div class="contact-band">
    <p class="address">12345, Address Goes Here<br>Country Name, 123456.</p>
    <ul class="contact-list">
      <li><svg viewBox="0 0 12 12" aria-hidden="true"><path d="M3 0h6a1 1 0 0 1 1 1v10a1 1 0 0 1-1 1H3a1 1 0 0 1-1-1V1a1 1 0 0 1 1-1zm0 1.5v8h6v-8zM6 10.2a.6.6 0 1 0 0 1.2.6.6 0 0 0 0-1.2z"/></svg>044-123 456 789</li>
      <li><svg viewBox="0 0 12 12" aria-hidden="true"><path d="M2.4 0.5l2 2.2-1 1.4c.7 1.6 2 2.9 3.6 3.6l1.4-1 2.2 2-1 2.3C5 11 1 7 0.1 1.6z"/></svg>044-123 456 789</li>
      <li><svg viewBox="0 0 12 12" aria-hidden="true"><path d="M0 2h12v8H0zm1 1v.4l5 3.2 5-3.2V3z"/></svg>info@brasswheel.ca</li>
      <li><svg viewBox="0 0 12 12" aria-hidden="true"><path d="M6 0a6 6 0 1 0 0 12A6 6 0 0 0 6 0zm-1 1.6c-.6.8-.9 1.6-.9 2.4l-2.6-.2A4.6 4.6 0 0 1 5 1.6zM1.4 5.2l2.6.2.1 2.2L2 8.4a4.5 4.5 0 0 1-.6-3.2zm4.8 5.3c.8-.9 1.4-2 1.6-3.2l2.6.4a4.6 4.6 0 0 1-4.2 2.8zM8 5.8 5.4 5.4 5.5 3c1.4.3 2.4 1.4 2.5 2.8z"/></svg>www.brasswheelservicing.ca</li>
    </ul>
    <span class="brand-mark-front">BWS</span>
  </div>
</section>

<section class="card card-back" aria-label="Business card back">
  <span class="brand-mark-back">BWS</span>
  <h2 class="company-stack">Brass<br>Wheel<br>Servicing</h2>
  <p class="tagline">When your gym gear runs out of steam, our crew is one call away!</p>
</section>

</body>
</html>
```